New Innovative Counselling and psychotherapy Service needs Business Card design

Keep it simple and professional. On one side, just company name and logo (perhaps in all blue) and maybe a tag line.

On other side (all white) my name and Qualifications in centre

Industry/Entity Type

Health And Wellness

Contact Information for Business Card

Derek Hollis
Counsellor & Psychotherapist
BSc (Psychol.), BA, Dip. (Couns. & Psych.), PG.Cert (CBT), MGVrA, NWTF

I will also require Mobile no, Email and web site address of which I'll pass on to final designer.

Font styles to use
Sans Serif

Requirements
Must have
• My Logo Only and please use the colours in logo that is in it.
Should not have
• Any other images

```html
<!DOCTYPE html>
<html lang="en">
<head>
<meta charset="utf-8">
<title>Kindred Path – Business Card</title>
<link rel="stylesheet" href="https://fonts.googleapis.com/css2?family=Roboto:wght@400;500&family=Roboto+Condensed:wght@400;700&display=swap">
<style>
  :root {
    --backdrop: #2b2b2b;
    --sky: #45b3ec;
    --leaf: #8fd35a;
    --paper: #f1f1f1;
    --white: #ffffff;
    --ink: #3a3a3a;
  }
  html, body {
    margin: 0;
    width: 1200px;
    height: 960px;
    overflow: hidden;
    background: var(--backdrop);
  }
  .canvas {
    position: relative;
    width: 1200px;
    height: 960px;
  }
  .card {
    position: absolute;
    width: 600px;
    height: 342px;
    overflow: hidden;
    box-shadow: 0 3px 8px rgba(0,0,0,.5);
  }
  .card--front { left: 322px; top: 110px; background: var(--paper); }
  .card--back  { left: 320px; top: 493px; background: var(--sky); }

  .front-backdrop {
    position: absolute;
    inset: 0;
    background: linear-gradient(to bottom, var(--sky) 0%, var(--sky) 55%, var(--paper) 80%, var(--paper) 100%);
  }

  .identity {
    position: absolute;
    left: 31px;
    top: 30px;
    color: var(--white);
    font-family: "Roboto Condensed", sans-serif;
  }
  .identity__name { margin: 0; font-size: 22px; font-weight: 700; line-height: 1.1; }
  .identity__role { margin: 2px 0 3px; font-size: 14.5px; font-weight: 700; }
  .identity__quals { margin: 0; font-size: 12.5px; line-height: 1.25; }

  .contact {
    position: absolute;
    left: 31px;
    top: 112px;
    margin: 0;
    padding: 0;
    list-style: none;
    color: var(--white);
    font-family: "Roboto", sans-serif;
    font-size: 14px;
  }
  .contact li { display: flex; align-items: center; height: 19.5px; }
  .contact svg { width: 14px; height: 14px; margin-right: 8px; fill: var(--white); }

  .brand {
    position: absolute;
    left: 320px;
    top: 262px;
    display: flex;
    align-items: center;
    font-family: "Roboto", sans-serif;
    font-size: 23px;
    font-weight: 400;
    color: var(--ink);
  }
  .brand__dot {
    width: 38px; height: 38px; border-radius: 50%;
    background: var(--sky);
    margin-right: 14px;
  }

  .back-brand {
    position: absolute;
    left: 0; right: 0;
    top: 125px;
    display: flex;
    justify-content: center;
    align-items: center;
    font-family: "Roboto", sans-serif;
    font-size: 40px;
    font-weight: 400;
    color: var(--white);
  }
  .back-brand__dot {
    width: 34px; height: 34px; border-radius: 50%;
    background: var(--leaf);
    margin-right: 16px;
  }
  .tagline {
    position: absolute;
    left: 0; right: 0;
    top: 287px;
    margin: 0;
    text-align: center;
    font-family: "Roboto", sans-serif;
    font-size: 14.5px;
    color: var(--white);
  }
</style>
</head>
<body>
<main class="canvas">
  <section class="card card--front">
    <div class="front-backdrop" role="img" aria-label="Decorative blue, white and green flowing wave band"></div>

    <header class="identity">
      <h1 class="identity__name">DEREK HOLLIS</h1>
      <p class="identity__role">COUNSELLOR &amp; PSYCHOTHERAPIST</p>
      <p class="identity__quals">BSc (Psychol.), BA, Dip. (Couns. &amp; Psych.)<br>PG.Cert (CBT), MGVrA,</p>
    </header>

    <ul class="contact">
      <li><svg viewBox="0 0 14 14"><rect x="3" y="0.5" width="8" height="13" rx="1.5"/><rect x="4.5" y="2" width="5" height="8.5" fill="var(--sky)"/></svg>555 014 2738</li>
      <li><svg viewBox="0 0 14 14"><path d="M1,3 H13 V11 H1 Z"/><path d="M1,3 L7,8 L13,3" fill="none" stroke="var(--sky)" stroke-width="1.2"/></svg>derek@Kindredpath.com</li>
      <li><svg viewBox="0 0 14 14"><circle cx="7" cy="7" r="6"/><path d="M4,4 Q6,5 5,7 Q8,8 7,11 M9,3 Q10,5 11,6" fill="none" stroke="var(--sky)" stroke-width="1.2"/></svg>www.Kindredpath.com</li>
    </ul>

    <div class="brand"><span class="brand__dot"></span>Kindred Path</div>
  </section>

  <section class="card card--back">
    <div class="back-brand"><span class="back-brand__dot"></span>Kindred Path</div>
    <p class="tagline">Caring For Your Psychological Well-Being Is Our Top Priority</p>
  </section>
</main>
</body>
</html>
```